Calm and Compass Health Flyer (new business startup)

One page...clear enough to be read if faxed. This mental health clinic treats depression/anxiety in kids and adults. It also treats opiate and alcohol addiction. It's in downtown Elmira, NY and the owner of the clinic is from Elmira NY, where it's located. This clinic does not take health insurance, so it charges a low rate of $75 a visit once they pay the $125 starting fee.

Target Market(s)

doctors offices, new patients

Industry/Entity Type

Doctor

Requirements
Must have
• see microsoft word document. pdf is printed on the company letterhead.
Nice to have
• a simplified map would be nice. if you can include the building it would be a plus. The same two fonts were used in the business cards and letter head (kennedy small caps boo*) and Refrigerator Delux.

```html
<!DOCTYPE html>
<html lang="en">
<head>
<meta charset="utf-8">
<title>Calm and Compass Health Flyer</title>
<link href="https://fonts.googleapis.com/css2?family=Roboto+Condensed:wght@700&family=Oswald:wght@400;500&family=Cormorant+SC:wght@500;600&display=swap" rel="stylesheet">
<style>
  :root {
    --blue: #2fa8df;
    --blue-deep: #2a8fd0;
    --orange: #ef6a34;
    --orange-soft: #f3a277;
    --ink: #1d1d1d;
    --paper: #ffffff;
    --map: #e9ebee;
    --brick: #8a4a35;
  }
  html, body { margin: 0; padding: 0; overflow: hidden; background: #f2f2f2; }
  .flyer {
    position: relative; width: 720px; height: 1200px; overflow: hidden;
    background: var(--paper); font-family: "Oswald", sans-serif; color: var(--ink);
  }
  .flyer > * { position: absolute; }
  .swoosh { left: 0; width: 720px; }
  .swoosh--top { top: 0; height: 150px; }
  .swoosh--bottom { bottom: 0; height: 130px; }

  .brand { top: 108px; left: 40px; display: flex; align-items: center; gap: 16px; }
  .brand__dot { width: 74px; height: 74px; border-radius: 50%; background: var(--orange); }
  .brand__name { font-family: "Roboto Condensed", sans-serif; font-weight: 700; font-size: 38px; color: var(--orange); letter-spacing: -0.5px; }

  .practice { top: 180px; left: 0; width: 740px; text-align: center; font-family: "Cormorant SC", serif; font-weight: 500; font-size: 31px; color: var(--blue-deep); margin: 0; }
  .contact { top: 226px; left: 0; width: 720px; text-align: center; font-size: 16px; color: var(--blue-deep); margin: 0; letter-spacing: 0.1px; }

  .building { left: -223px; top: 305px; width: 500px; height: 500px; border-radius: 50%;
    background: linear-gradient(160deg, #c9d7e6 0%, #a0614a 35%, var(--brick) 70%, #7e8790 100%);
    box-shadow: 0 0 0 9px var(--blue); }
  .quote { left: 136px; top: 672px; width: 176px; height: 176px; border-radius: 50%; background: rgba(240,150,100,0.88);
    display: flex; align-items: center; }
  .quote p { margin: 0 0 0 26px; font-size: 18px; line-height: 27px; color: var(--ink); }

  .hours { left: 270px; top: 286px; width: 470px; height: 120px; border-radius: 30px 0 0 30px;
    background: linear-gradient(90deg, var(--orange) 0%, #f5b18c 55%, #bcdaf0 100%); }
  .hours__inner { position: absolute; left: 12px; top: 12px; right: 0; bottom: 12px; border-radius: 20px 0 0 20px; background: var(--paper);
    display: flex; align-items: center; justify-content: center; font-size: 25px; font-weight: 500; padding-right: 30px; }

  .service { top: 428px; width: 200px; text-align: center; font-size: 20px; margin: 0; }
  .service--eval { left: 277px; }
  .service--visit { left: 490px; }

  .price-card { top: 469px; width: 157px; height: 344px; border: 2px solid var(--orange); border-top: none; border-radius: 0 0 10px 10px; box-sizing: border-box; overflow: hidden; background: var(--paper); }
  .price-card--eval { left: 300px; }
  .price-card--visit { left: 519px; }
  .price-card__head { height: 112px; position: relative; }
  .price-card__head svg { position: absolute; inset: 0; }
  .price-card__label { position: absolute; left: 18px; top: 22px; font-size: 29px; color: var(--paper); font-weight: 500; }
  .price-card__time { text-align: center; font-family: "Cormorant SC", serif; font-weight: 500; color: var(--blue-deep); font-size: 38px; line-height: 44px; margin-top: 10px; height: 122px; }
  .price-card__cost { background: var(--orange); color: var(--paper); height: 72px; display: flex; align-items: center; justify-content: center; font-family: "Cormorant SC", serif; font-weight: 600; font-size: 36px; }

  .ages { top: 822px; left: 380px; font-size: 27px; margin: 0; }
  .conditions { top: 864px; left: 20px; width: 420px; font-size: 22px; line-height: 42px; margin: 0; }
  .conditions strong { font-weight: 500; font-size: 27px; }
  .disclaimer { top: 972px; left: 20px; width: 350px; font-size: 12px; line-height: 19px; margin: 0; }
  .office { top: 1038px; left: 28px; font-size: 16px; color: var(--blue-deep); margin: 0; word-spacing: 2px; }
  .office span { margin-left: 14px; }
  .associate { top: 1074px; left: 96px; font-family: "Cormorant SC", serif; font-size: 19px; color: var(--blue-deep); margin: 0; }
  .website { top: 1103px; left: 142px; font-size: 14px; color: var(--blue-deep); margin: 0; }

  .map { left: 312px; top: 882px; width: 620px; height: 620px; border-radius: 50%; background: linear-gradient(135deg, #e6e8ec 0%, #eef0f2 50%, #dfe7ef 100%); box-shadow: 0 0 0 9px var(--blue); }
  .address { left: 491px; top: 1084px; width: 229px; height: 87px; background: rgba(47,168,223,0.85); color: var(--paper); font-size: 25px; line-height: 34px; padding: 9px 0 0 18px; box-sizing: border-box; margin: 0; }
</style>
</head>
<body>
<main class="flyer">
  <svg class="swoosh swoosh--top" viewBox="0 0 720 150" preserveAspectRatio="none" aria-hidden="true">
    <defs>
      <linearGradient id="topStripe" x1="0" x2="1">
        <stop offset="0" stop-color="#ef6a34"/><stop offset="0.45" stop-color="#fbe3d6"/><stop offset="1" stop-color="#ef6a34"/>
      </linearGradient>
    </defs>
    <path d="M0 0H720V118C560 40 250 20 0 62Z" fill="#2fa8df"/>
    <path d="M0 62C250 20 560 40 720 118V134C560 58 250 36 0 74Z" fill="url(#topStripe)"/>
  </svg>

  <div class="brand">
    <span class="brand__dot"></span>
    <span class="brand__name">Calm and Compass Health</span>
  </div>
  <p class="practice">Daniel Reyes, RPA, PLLC</p>
  <p class="contact">(607)-555-0142 • Psychiatric Physician Assistant (PA-C, PSY-CAQ) • dreyes@calmcompass.example</p>

  <div class="building" role="img" aria-label="Photo of the downtown brick office building on the street corner"></div>
  <div class="quote"><p>“We work for you,<br>not the insurance<br>companies”</p></div>

  <div class="hours"><div class="hours__inner">Hours: Monday and Saturdays 9-4 PM</div></div>

  <p class="service service--eval">Psychiatric Evaluation</p>
  <p class="service service--visit">Psychiatric Office Visit</p>

  <div class="price-card price-card--eval">
    <div class="price-card__head">
      <svg viewBox="0 0 157 112" preserveAspectRatio="none" aria-hidden="true">
        <defs><linearGradient id="cardHead" x1="0" y1="0" x2="1" y2="1"><stop offset="0.3" stop-color="#2fa8df"/><stop offset="0.6" stop-color="#ffffff"/><stop offset="0.85" stop-color="#ef6a34"/></linearGradient></defs>
        <path d="M10 0H147L157 10V70C110 90 40 95 0 112V10Z" fill="url(#cardHead)"/>
      </svg>
      <span class="price-card__label">Price</span>
    </div>
    <div class="price-card__time">45<br>Minutes</div>
    <div class="price-card__cost">$125</div>
  </div>

  <div class="price-card price-card--visit">
    <div class="price-card__head">
      <svg viewBox="0 0 157 112" preserveAspectRatio="none" aria-hidden="true">
        <path d="M10 0H147L157 10V70C110 90 40 95 0 112V10Z" fill="url(#cardHead)"/>
      </svg>
      <span class="price-card__label">Price</span>
    </div>
    <div class="price-card__time">15<br>Minutes</div>
    <div class="price-card__cost">$75</div>
  </div>

  <p class="ages">Ages:&nbsp; 6 years old and up</p>
  <p class="conditions"><strong>Conditions Treated:</strong>&nbsp; Depression, Anxiety, PTSD, ADHD, Addiction, Bipolar, Childhood</p>
  <p class="disclaimer">*Although we do not partner with any Health Insurance Companies at this time, a bill will be provided to you at the time of service for you to submit to your insurance company.</p>

  <div class="map" role="img" aria-label="Street map of downtown Elmira showing the clinic location"></div>
  <p class="address">240 N. Market #310<br>Elmira, NY 14901</p>

  <svg class="swoosh swoosh--bottom" viewBox="0 0 720 130" preserveAspectRatio="none" aria-hidden="true">
    <defs>
      <linearGradient id="bottomStripe" x1="0" x2="1">
        <stop offset="0" stop-color="#ef6a34"/><stop offset="1" stop-color="#fbe3d6"/>
      </linearGradient>
    </defs>
    <path d="M0 36C100 80 220 110 330 120V130H0Z" fill="#2fa8df"/>
    <path d="M0 14C100 62 220 96 330 110V120C220 110 100 80 0 36Z" fill="url(#bottomStripe)"/>
  </svg>

  <p class="office">Phone: (607)-555-0142<span>FAX: 607-555-0178</span></p>
  <p class="associate">with Dr. Helen Marsh</p>
  <p class="website">www.calmcompass.example</p>
</main>
</body>
</html>
```